Business Card / Appointment Card for Physician

On one side it should give the logo, address, and contact information, and on the other side it should br an Appointment card.

One Side:
Logo (see attached files)
Board Certified American Orthopedic Surgery

1874 Larkmoor Ave.
Suite KP7
Bronx, NY 10287
Tel: (718) 555 - 0142
Fax: (718) 555 - 0187

612 Ninth Ave.
Suite 42
New York, NY 10089
Tel: (212) 555 - 0163

Second Side:
Appointment
give them a choice of Bronx or Mahattan office
For:
Date:
Time:

If you are unable to keep your appointment, please call (718) 555-0129 24hrs in advance.

Target Market(s)

People that need orthopedic surgery

Industry/Entity Type

Business

Contact Information for Business Card

smart and attractive

Requirements
Must have
• logo
• contact information on one side, appointment information on the other

```html
<!DOCTYPE html>
<html lang="en">
<head>
<meta charset="utf-8">
<title>Daniel R. Hollister MD PC – Business and Appointment Card</title>
<link href="https://fonts.googleapis.com/css2?family=Montserrat:wght@400;500;600&display=swap" rel="stylesheet">
<style>
  :root {
    --stage: #2a2d30;
    --card-light: #ffffff;
    --card-dark: #1e1f22;
    --ink-dark: #2b2b2b;
    --ink-light: #f2f2f2;
    --accent-blue: #1aa3e0;
    --accent-green: #5aa83c;
    --rule-light: #d9d9d9;
  }
  * { box-sizing: border-box; margin: 0; padding: 0; }
  html, body { width: 1200px; height: 738px; overflow: hidden; }
  body {
    background: var(--stage);
    font-family: "Montserrat", Arial, sans-serif;
    display: flex;
    align-items: center;
    justify-content: center;
    gap: 48px;
  }
  .card {
    position: relative;
    width: 525px;
    height: 300px;
    border-radius: 3px;
    overflow: hidden;
    box-shadow: 0 14px 30px rgba(0,0,0,.45);
  }

  /* Appointment side */
  .card--appointment { background: var(--card-light); color: var(--ink-dark); }
  .appointment__title {
    position: absolute; top: 52px; left: 0; right: 0;
    text-align: center; color: var(--accent-blue);
    font-size: 17px; font-weight: 500; letter-spacing: .5px;
  }
  .appointment__fields { position: absolute; top: 96px; left: 48px; right: 48px; }
  .field {
    display: flex; align-items: flex-end; gap: 10px;
    height: 38px; color: var(--accent-blue); font-size: 13px;
  }
  .field__label { width: 42px; }
  .field__line { flex: 1; border-bottom: 1px solid var(--accent-blue); margin-bottom: 3px; }
  .appointment__note {
    position: absolute; bottom: 28px; left: 0; right: 0;
    text-align: center; font-size: 11px; color: var(--ink-dark);
  }
  .appointment__note .phone { color: var(--accent-blue); font-weight: 500; }

  /* Contact side */
  .card--contact { background: linear-gradient(135deg, #26272a 0%, var(--card-dark) 60%, #191a1c 100%); color: var(--ink-light); }
  .brand {
    position: absolute; top: 30px; left: 36px;
    display: flex; align-items: center; gap: 12px;
  }
  .brand__dot { width: 34px; height: 34px; border-radius: 50%; background: var(--accent-blue); }
  .brand__name { color: var(--accent-blue); font-size: 15px; font-weight: 500; letter-spacing: .4px; text-transform: uppercase; }
  .doctor {
    position: absolute; top: 96px; right: 36px; text-align: right;
  }
  .doctor__name { color: var(--accent-blue); font-size: 19px; font-weight: 500; }
  .doctor__title { font-size: 12px; color: var(--ink-light); margin-top: 2px; }
  .divider {
    position: absolute; top: 138px; left: 36px; right: 90px;
    border-top: 1px solid var(--rule-light);
  }
  .office { position: absolute; font-size: 13.5px; line-height: 1.4; }
  .office--bronx { top: 152px; left: 36px; }
  .office--manhattan { top: 146px; right: 36px; text-align: right; }
  .office .label { color: var(--accent-blue); font-weight: 500; }
  .swoosh { position: absolute; left: 0; bottom: 0; width: 525px; height: 70px; }
</style>
</head>
<body>

  <section class="card card--appointment" aria-label="Appointment card">
    <h2 class="appointment__title">Appointment:</h2>
    <div class="appointment__fields">
      <div class="field"><span class="field__label">For:</span><span class="field__line"></span></div>
      <div class="field"><span class="field__label">Date:</span><span class="field__line"></span></div>
      <div class="field"><span class="field__label">Time:</span><span class="field__line"></span></div>
    </div>
    <p class="appointment__note">If you are unable to keep your appointment, please <span class="phone">call (718) 555-0129</span> 24hrs in advance.</p>
  </section>

  <section class="card card--contact" aria-label="Business card">
    <div class="brand">
      <span class="brand__dot"></span>
      <span class="brand__name">Daniel R. Hollister MD PC</span>
    </div>
    <div class="doctor">
      <div class="doctor__name">Dr. Daniel Hollister</div>
      <div class="doctor__title">MD</div>
    </div>
    <div class="divider"></div>
    <address class="office office--manhattan" style="font-style:normal">
      612 Ninth Ave.<br>
      Suite 42 New York, NY 10089<br>
      <span class="label">Tel:</span> (212) 555 - 0163
    </address>
    <address class="office office--bronx" style="font-style:normal; top:196px">
      1874 Larkmoor Ave.<br>
      Suite KP7 Bronx, NY 10287<br>
      <span class="label">Tel:</span> (718) 555 - 0142<br>
      <span class="label">Fax:</span> (718) 555 - 0187
    </address>
    <svg class="swoosh" viewBox="0 0 525 70" preserveAspectRatio="none" aria-hidden="true">
      <path d="M0 52 L340 40 C370 38 380 30 400 26 L525 22 L525 24 L400 30 C380 34 370 42 340 44 L0 56 Z" fill="var(--accent-green)"/>
      <path d="M0 58 L350 48 C385 46 395 30 420 26 L525 22 L525 36 L430 38 C400 40 390 58 350 60 L0 68 Z" fill="var(--accent-blue)"/>
    </svg>
  </section>

</body>
</html>
```